Advertisement Coaching practice

I need an advertisement (to be printed in newspaper). I have a coaching practice where I offer coaching, workshops family constellations and relationship therapy. The ad needs to express calmness, inspiration to transform but also not dull and boring. It would be great if you could use the colors from my logo into the ad.

Dimensions are: 13,04 cm Width x 9,72 cm Height.

I will add my previous self-made ad, my company logo, a portrait photo of myself and the text I want to add. Also my contact details should be visible as well.

Requirements
Nice to have
• I have updated the brief with a flyer that I had previously made by a designer. It would be a nice to have if the ad ties in with that. You can also look at my website at www.bravemoor.nu to see what colors I used there.

```html
<!DOCTYPE html>
<html lang="nl">
<head>
<meta charset="utf-8">
<title>Advertentie – coaching praktijk</title>
<link href="https://fonts.googleapis.com/css2?family=Roboto:wght@900&family=Roboto+Condensed:wght@300;400;700&display=swap" rel="stylesheet">
<style>
  :root {
    --backdrop: #8f9d9d;
    --violet: #7f5af0;
    --white: #ffffff;
    --mint: #5dd3ad;
    --orange: #f7a54a;
    --skin: #b07a5c;
    --hair: #3a3430;
  }
  * { margin: 0; padding: 0; box-sizing: border-box; }
  html, body { width: 846px; height: 1200px; overflow: hidden; }
  body {
    background: var(--backdrop);
    font-family: "Roboto Condensed", sans-serif;
    position: relative;
  }
  .ad {
    position: absolute;
    left: 33px; top: 310px;
    width: 780px; height: 581px;
    background: var(--violet);
    color: var(--white);
    overflow: hidden;
    border: 1px solid #2a2a2a;
    box-shadow: 6px 8px 14px rgba(0,0,0,.35);
  }
  .portrait {
    position: absolute; left: 0; top: 0;
    width: 780px; height: 500px;
  }
  .headline {
    position: absolute; left: 41px; top: 28px;
    font-family: "Roboto", sans-serif;
    font-weight: 900;
    font-size: 29px;
    line-height: 32px;
    letter-spacing: 1.2px;
  }
  .intro {
    position: absolute; left: 41px; top: 137px; width: 400px;
    font-weight: 300; font-size: 16.5px; line-height: 20px;
  }
  .support-box {
    position: absolute; left: 41px; top: 190px;
    width: 380px; height: 128px;
    background: var(--white);
    border: 2px solid var(--white);
    outline: 2px solid var(--white);
    outline-offset: -6px;
    border-radius: 0 26px 0 26px;
    color: var(--violet);
    padding: 13px 20px 0 28px;
    box-shadow: inset 0 0 0 4px var(--violet);
  }
  .support-box h2 {
    font-weight: 700; font-size: 16px; line-height: 20px;
  }
  .support-box ul { list-style: none; }
  .support-box li {
    font-size: 16px; line-height: 20.5px;
    padding-left: 12px; position: relative;
  }
  .support-box li::before { content: "•"; position: absolute; left: 0; font-size: 12px; }
  .offer {
    position: absolute; left: 41px; top: 334px; width: 400px;
    font-weight: 300; font-size: 16px; line-height: 20.3px;
  }
  .brand {
    position: absolute; left: 60px; top: 452px; width: 160px;
    text-align: center;
  }
  .brand-dot {
    width: 42px; height: 42px; border: 2px solid var(--white); border-radius: 50%;
    margin: 0 auto 10px;
  }
  .brand-name {
    font-weight: 400; font-size: 30px; line-height: 32px; letter-spacing: 1px;
  }
  .contact-band {
    position: absolute; left: 263px; top: 500px;
    width: 517px; height: 81px;
    background: var(--mint);
    border-top-left-radius: 34px;
    text-align: right;
    padding: 16px 36px 0 0;
  }
  .contact-name { font-weight: 700; font-size: 16px; line-height: 20px; }
  .contact-line { font-weight: 400; font-size: 16px; line-height: 24px; }
</style>
</head>
<body>
  <div class="ad">
    <svg class="portrait" viewBox="0 0 780 500" role="img" aria-label="Portretfoto van de coach, vrouw met donker haar, tegen een oranje achtergrond">
      <defs>
        <radialGradient id="portraitTone" cx="0.68" cy="0.5" r="0.6">
          <stop offset="0" stop-color="var(--skin)"/>
          <stop offset="0.55" stop-color="#c98a5a"/>
          <stop offset="1" stop-color="var(--orange)"/>
        </radialGradient>
      </defs>
      <path d="M551 0 H780 V500 H500 C470 420 455 300 470 200 C480 120 510 50 551 0 Z" fill="var(--orange)"/>
      <path d="M590 0 H780 V500 H540 C520 380 540 200 590 0 Z" fill="url(#portraitTone)"/>
    </svg>

    <h1 class="headline">COACHING,<br>FAMILIEOPSTELLINGEN &amp;<br>RELATIETHERAPIE</h1>

    <p class="intro">Trauma’s en negatieve ervaringen vormen ons en blijven nog lang voelbaar. Ze kunnen groei of geluk in de weg staan.</p>

    <div class="support-box">
      <h2>IK BEN AMARA EN ONDERSTEUN JE BIJ HET:</h2>
      <ul>
        <li>Doorbreken van belemmerende patronen;</li>
        <li>Beter omgaan met conflicten;</li>
        <li>In gezonde verbinding met elkaar als koppel<br>of met anderen komen;</li>
      </ul>
    </div>

    <p class="offer">Maandelijks geef ik workshops familieopstellingen. Ook houd ik themasessies rond adoptie, moeder-dochterdyna­miek of relaties. Ook bied ik individuele coaching, relatie­therapie en retraites aan. Kijk op de website voor meer info of neem contact op en ontdek wat het beste bij jou past.</p>

    <div class="brand">
      <div class="brand-dot"></div>
      <div class="brand-name">bravemoor</div>
    </div>

    <div class="contact-band">
      <div class="contact-name">Amara Veldkamp</div>
      <div class="contact-line">Email: info@bravemoor.nu &nbsp;|&nbsp; Tel: 06-41 27 58 93 &nbsp;|&nbsp; www.bravemoor.nu</div>
    </div>
  </div>
</body>
</html>
```